Rebrand/migrate of website to Wordpress

Rebrand/transfer of php website to new wordpress website using the Noxel theme. Dial4LessLines.com is being rebranded to Quorvix and therefore we are looking to simplify the current layout to match competitors sites and be mobile device friendly.
The new site will need to show services in a clear uncluttered way with more emphasis on the service rather than large amounts of text. See attachment B1 for example.
Competitors sites are kx.com , ringmoor.co.uk, zelwire.com
Updates

As I have had a few request from designers to extend the deadline. I have requested Pixel Harbor to extend to Tuesday 3rd April 2018

Target Market(s)

UK Home phone and small business customers

Industry/Entity Type

Telecom

Coding

Coded - Design and coding required

Number of Pages Required

5+ page

Colors

Designer to choose colors to be used in the design.

Requirements
Must have
• 1. Use Noxel wordpress theme that will be supplied.
• 2. Combine the best layouts where possible as used by competitors but in a unique way.
• 3. Horizontal bar should be in white so that it can layer over banner as per file A1.
• 4. Simplify current layout to match competitors see attached file B1.
• 5. Integrate Tallbranch - Tallbranch Leads Web / web form to capture interested customers - name, Company name, Telephone number, email address.
Should not have
• Colour scheme that is the same as our competitors RingMoor, KX, Halden, Vexa Net

```html
<!DOCTYPE html>
<html lang="en">
<head>
<meta charset="utf-8">
<title>Quorvix – Cheaper Calls</title>
<link href="https://fonts.googleapis.com/css2?family=Open+Sans:wght@400;600;700&family=Montserrat:wght@600;700&display=swap" rel="stylesheet">
<style>
:root{
  --pink:#e8307c;
  --blue:#22a5dc;
  --blue-dark:#1790c4;
  --footer:#25272c;
  --footer-bar:#1b1c20;
  --field:#3a3d43;
  --ink:#333840;
  --line:#e3e6ea;
  --white:#ffffff;
}
*{margin:0;padding:0;box-sizing:border-box}
html,body{width:814px;height:1200px;overflow:hidden}
body{font-family:"Open Sans",Arial,sans-serif;color:var(--ink);background:var(--white);font-size:8px;line-height:1.45}
h1,h2,h3,h4{font-family:"Montserrat",Arial,sans-serif}
.page{width:814px;height:1200px;display:flex;flex-direction:column}

/* hero */
.hero{position:relative;height:165px;flex:none;background:linear-gradient(90deg,#15181e 0%,#262a33 50%,#3a3a40 100%);color:var(--white);overflow:hidden}
.hero-photo{position:absolute;right:0;top:0;width:380px;height:165px;background:radial-gradient(ellipse at 55% 45%,#d9b8a6 0%,#8a6a5c 35%,#3a3a40 75%)}
.topbar{position:absolute;top:0;left:0;right:0;height:30px;display:flex;align-items:center;justify-content:space-between;padding:0 84px 0 92px}
.brand{display:flex;align-items:center;gap:5px;font-weight:700;font-size:11px;color:var(--white)}
.brand-dot{width:9px;height:9px;border-radius:50%;background:var(--pink)}
.nav{display:flex;gap:3px}
.nav a{color:var(--white);text-decoration:none;font-size:7px;padding:4px 7px;border:1px solid rgba(255,255,255,.35)}
.nav a.active{background:var(--pink);border-color:var(--pink)}
.hero-copy{position:absolute;left:92px;top:48px;width:320px}
.hero-copy h1{font-size:18px;line-height:1.2;font-weight:700}
.hero-copy h1 span{background:var(--pink);padding:0 4px}
.hero-copy p{margin-top:6px;font-size:7px;color:#d5d8de;width:240px}
.hero-phone{margin-top:7px;font-weight:700;font-size:9px}
.btn{display:inline-block;background:var(--pink);color:var(--white);font-size:7px;font-weight:600;padding:5px 12px;border-radius:2px}
.hero-copy .btn{margin-top:6px}

/* home saver */
.saver{height:225px;flex:none;background:var(--pink);color:var(--white);position:relative;padding:20px 92px}
.saver h2{font-size:12px}
.saver .lead{font-weight:700;font-size:8px;margin-top:5px}
.saver .intro{width:280px;font-size:6.5px;margin-top:4px;color:#fbe0ec}
.checks{list-style:none;margin-top:5px}
.checks li{display:flex;align-items:center;gap:4px;font-size:6.5px;margin-bottom:2px}
.checks svg{width:7px;height:7px}
.mini-rates{width:200px;margin-top:6px;border-collapse:collapse;font-size:6.5px}
.mini-rates td{padding:2.5px 6px;border-bottom:1px solid rgba(255,255,255,.3)}
.mini-rates td:last-child{text-align:right;font-weight:700}
.saver-photo-a{position:absolute;left:414px;top:26px;width:118px;height:76px;background:linear-gradient(135deg,#f4f1ee,#c7b8ae);border:3px solid var(--white)}
.saver-photo-b{position:absolute;left:484px;top:96px;width:170px;height:104px;background:linear-gradient(135deg,#d8c3b4,#7d6e6a);border:3px solid var(--white)}

/* rates */
.rates{height:395px;flex:none;padding:18px 90px 0}
.rates h2{font-size:12px;margin-bottom:9px}
.rate-table{width:100%;border-collapse:collapse;font-size:6.5px}
.rate-table th{background:var(--blue);color:var(--white);text-align:left;padding:4px 8px;font-weight:600}
.rate-table td{padding:2.4px 8px;border-bottom:1px solid var(--line);color:#555b63}
.rate-table tr:nth-child(even) td{background:#f6f7f9}
.rate-table th:not(:first-child),.rate-table td:not(:first-child){width:70px}

/* news */
.news{height:220px;flex:none;background:linear-gradient(180deg,var(--blue) 0%,var(--blue-dark) 100%);padding:18px 152px 0;color:var(--white)}
.news h2{text-align:center;font-size:12px;margin-bottom:12px}
.cards{display:flex;gap:9px}
.card{width:164px}
.card-photo{height:95px;background:linear-gradient(135deg,#c9b7a8,#5b5f66)}
.card-photo.b{background:linear-gradient(135deg,#9aa4ae,#3e4650)}
.card-photo.c{background:linear-gradient(135deg,#e1c9b4,#7a6456)}
.card h3{font-size:8px;margin-top:7px;line-height:1.3}
.card .meta{font-size:6px;color:#d8eef9;margin-top:4px}

/* footer */
.footer{flex:1;background:var(--footer);color:#aeb3ba;display:flex;flex-direction:column}
.footer-cols{flex:1;display:flex;gap:20px;padding:16px 92px 0}
.fcol{width:140px;font-size:6px}
.fcol h4{color:var(--white);font-size:8px;margin-bottom:6px}
.fcol .brand{font-size:9px;margin-bottom:6px}
.lead-form{display:flex;flex-direction:column;gap:3px}
.field{height:13px;background:var(--field);color:#8d929a;font-size:6px;line-height:13px;padding:0 5px}
.lead-form .btn{align-self:flex-start;margin-top:2px;padding:3px 10px;font-size:6px}
.posts li{list-style:none;margin-bottom:4px;padding-left:6px;position:relative}
.posts li::before{content:"";position:absolute;left:0;top:3px;width:2px;height:2px;background:var(--pink)}
.footer-bar{height:22px;background:var(--footer-bar);display:flex;align-items:center;justify-content:space-between;padding:0 92px;font-size:6px}
.footer-links{display:flex;gap:9px}
.socials{display:flex;gap:4px}
.socials span{width:9px;height:9px;border-radius:50%;background:#4a4d54}
</style>
</head>
<body>
<div class="page">

  <header class="hero">
    <div class="hero-photo" role="img" aria-label="Photo of a smiling woman wearing earphones"></div>
    <div class="topbar">
      <div class="brand"><span class="brand-dot"></span>Quorvix</div>
      <nav class="nav">
        <a href="#">Home</a><a href="#">About Us</a><a href="#">Services</a>
        <a href="#" class="active">Rates</a><a href="#">Support</a><a href="#">Contact us</a>
      </nav>
    </div>
    <div class="hero-copy">
      <h1>Switch to <span>Cheaper</span> Calls Now!</h1>
      <p>Keep your number, lower your monthly bill and enjoy clear UK and international calls with simple plans for home and small business.</p>
      <div class="hero-phone">0800 000 4417</div>
      <span class="btn">Find Out More</span>
    </div>
  </header>

  <section class="saver">
    <h2>Home Saver UK Landline</h2>
    <div class="lead">Reduce the cost of your calls with unlimited weekend calls</div>
    <p class="intro">Our Home Saver plan gives you a reliable landline with low call rates, no long contract and friendly UK support whenever you need a hand with your line.</p>
    <ul class="checks">
      <li><svg viewBox="0 0 10 10"><path d="M1 5l3 3 5-6" stroke="#fff" stroke-width="1.8" fill="none"/></svg>Unlimited evening and weekend calls</li>
      <li><svg viewBox="0 0 10 10"><path d="M1 5l3 3 5-6" stroke="#fff" stroke-width="1.8" fill="none"/></svg>Keep your existing phone number</li>
      <li><svg viewBox="0 0 10 10"><path d="M1 5l3 3 5-6" stroke="#fff" stroke-width="1.8" fill="none"/></svg>No setup fee and quick switching</li>
    </ul>
    <table class="mini-rates">
      <tr><td>Monthly line rental</td><td>£11.99</td></tr>
      <tr><td>UK landline calls per min</td><td>3p</td></tr>
      <tr><td>UK mobile calls per min</td><td>9p</td></tr>
      <tr><td>Weekend calls</td><td>Free</td></tr>
    </table>
    <div class="saver-photo-a" role="img" aria-label="Photo of a cordless home phone on a desk"></div>
    <div class="saver-photo-b" role="img" aria-label="Photo of a woman talking on the phone at home"></div>
  </section>

  <section class="rates">
    <h2>International Rates</h2>
    <table class="rate-table">
      <thead><tr><th>Destination</th><th>Landline</th><th>Mobile</th><th>Weekend</th></tr></thead>
      <tbody>
        <tr><td>Australia</td><td>2p</td><td>6p</td><td>2p</td></tr>
        <tr><td>Belgium</td><td>3p</td><td>9p</td><td>3p</td></tr>
        <tr><td>Canada</td><td>1p</td><td>1p</td><td>1p</td></tr>
        <tr><td>China</td><td>2p</td><td>2p</td><td>2p</td></tr>
        <tr><td>Denmark</td><td>3p</td><td>8p</td><td>3p</td></tr>
        <tr><td>France</td><td>2p</td><td>7p</td><td>2p</td></tr>
        <tr><td>Germany</td><td>2p</td><td>8p</td><td>2p</td></tr>
        <tr><td>Greece</td><td>3p</td><td>10p</td><td>3p</td></tr>
        <tr><td>India</td><td>3p</td><td>3p</td><td>3p</td></tr>
        <tr><td>Ireland</td><td>2p</td><td>6p</td><td>2p</td></tr>
        <tr><td>Italy</td><td>2p</td><td>9p</td><td>2p</td></tr>
        <tr><td>Japan</td><td>4p</td><td>11p</td><td>4p</td></tr>
        <tr><td>Netherlands</td><td>2p</td><td>9p</td><td>2p</td></tr>
        <tr><td>Nigeria</td><td>7p</td><td>8p</td><td>7p</td></tr>
        <tr><td>Pakistan</td><td>6p</td><td>6p</td><td>6p</td></tr>
        <tr><td>Poland</td><td>2p</td><td>5p</td><td>2p</td></tr>
        <tr><td>Portugal</td><td>3p</td><td>9p</td><td>3p</td></tr>
        <tr><td>Spain</td><td>2p</td><td>7p</td><td>2p</td></tr>
        <tr><td>Sweden</td><td>2p</td><td>8p</td><td>2p</td></tr>
        <tr><td>Turkey</td><td>4p</td><td>10p</td><td>4p</td></tr>
        <tr><td>United States</td><td>1p</td><td>1p</td><td>1p</td></tr>
      </tbody>
    </table>
  </section>

  <section class="news">
    <h2>News and Articles</h2>
    <div class="cards">
      <article class="card">
        <div class="card-photo" role="img" aria-label="Photo of a man making a call in an office"></div>
        <h3>Lorem ipsum dolor sit amet, consectetur</h3>
        <div class="meta">By Admin · 12 March 2018</div>
      </article>
      <article class="card">
        <div class="card-photo b" role="img" aria-label="Photo of a business team around a table"></div>
        <h3>Lorem ipsum dolor sit amet, consectetur</h3>
        <div class="meta">By Admin · 08 March 2018</div>
      </article>
      <article class="card">
        <div class="card-photo c" role="img" aria-label="Photo of friends smiling at a phone"></div>
        <h3>Lorem ipsum dolor sit amet, consectetur</h3>
        <div class="meta">By Admin · 02 March 2018</div>
      </article>
    </div>
  </section>

  <footer class="footer">
    <div class="footer-cols">
      <div class="fcol">
        <div class="brand"><span class="brand-dot"></span>Quorvix</div>
        <p>Simple, low cost phone lines for UK homes and small businesses, with honest pricing and local support.</p>
      </div>
      <div class="fcol">
        <h4>Newsletter</h4>
        <form class="lead-form" action="#">
          <div class="field">Your name</div>
          <div class="field">Company name</div>
          <div class="field">Telephone number</div>
          <div class="field">Email address</div>
          <span class="btn">Sign Up</span>
        </form>
      </div>
      <div class="fcol">
        <h4>Recent Posts</h4>
        <ul class="posts">
          <li>How to switch your landline</li>
          <li>Cutting business call costs</li>
          <li>New low international rates</li>
        </ul>
      </div>
      <div class="fcol">
        <h4>Contact Info</h4>
        <p>14 Arden Row, Pellbury</p>
        <p>0800 000 4417</p>
        <p>hello@quorvix.co.uk</p>
      </div>
    </div>
    <div class="footer-bar">
      <div class="footer-links"><span>Home</span><span>About Us</span><span>Services</span><span>Rates</span><span>Support</span><span>Contact us</span></div>
      <div class="socials"><span></span><span></span><span></span></div>
    </div>
  </footer>

</div>
</body>
</html>
```